Logo Tweak & Full Set of Stationery

We need a redesign / tweaking of Logo for rebranding of our company. We are Australia's largest installer of commercial fencing and high security infrastructure. We also have divisions in security and civil works (infrastrucuture).

We would like to see designs that incorporate black, white & blue. Revamp of current Diamond Logo (including HC) would be ideal but open to all ideas.

Design needs to portray a highly professional & corporate image.

Required:
- Tweak / Redesign of Logo
- Letterhead
- email Signature
- Business Cards
- Presentation Folder

Address fields should be interchangeable to accomodate multiple locations.

Website: www.harvillecorp.com.au
Updates

Due to short turn around time for project - Fee increased to $500 AUD Guaranteed

Thanks

Designs are looking good
I have emailed those submitted thus far to the board to start short listing.

Please do not take offence if your design is eliminated as part of this process  - there are so many great concepts and if is difficult to pick between them.

Thanks
Dustin

Target Market(s)

Tier 1 / 2 Builders (ie.. Brick Arch Peter Farley) and Government related bodies

Industry/Entity Type

Security

Requirements
Must have
• Company Name: Harville Corp

Tag Line: Fencing * Security * Civil

Logo

```html
<!DOCTYPE html>
<html lang="en">
<head>
<meta charset="utf-8">
<title>Harville Corp Letterhead</title>
<link rel="stylesheet" href="https://fonts.googleapis.com/css2?family=Cabin:wght@400;500&display=swap">
<style>
  :root {
    --ink: #000000;
    --paper: #ffffff;
    --brand-white: #ffffff;
    --mark-grey: #262626;
    --text-dark: #1e1e1e;
    --text-mid: #4a4a4a;
  }
  html, body {
    margin: 0;
    padding: 0;
    width: 848px;
    height: 1200px;
    overflow: hidden;
    background: var(--paper);
  }
  .letterhead {
    position: relative;
    width: 848px;
    height: 1200px;
    background: var(--paper);
    font-family: "Cabin", "Gill Sans", sans-serif;
  }
  .header-band {
    position: absolute;
    left: 0;
    top: 0;
    width: 848px;
    height: 109px;
    background: var(--ink);
    overflow: hidden;
  }
  .brand-disc {
    position: absolute;
    left: 618px;
    top: 30px;
    width: 52px;
    height: 52px;
    border-radius: 50%;
    background: var(--mark-grey);
  }
  .brand-name {
    position: absolute;
    left: 686px;
    top: 50px;
    margin: 0;
    color: var(--brand-white);
    font-weight: 400;
    font-size: 18px;
    line-height: 19px;
    letter-spacing: 3px;
    text-transform: uppercase;
  }
  .brand-name span {
    display: block;
  }
  .brand-name .second-line {
    padding-left: 19px;
  }
  .office-address {
    position: absolute;
    right: 44px;
    top: 118px;
    margin: 0;
    text-align: right;
    font-style: normal;
    font-size: 12px;
    line-height: 17px;
    color: var(--text-mid);
  }
  .office-address span {
    display: block;
  }
  .office-address .office-name {
    color: var(--text-dark);
    font-weight: 500;
    font-size: 12.5px;
    letter-spacing: 0.6px;
    text-transform: uppercase;
  }
</style>
</head>
<body>
  <main class="letterhead">
    <header class="header-band">
      <div class="brand-disc"></div>
      <p class="brand-name">
        <span class="first-line">Harville</span>
        <span class="second-line">Corp</span>
      </p>
    </header>
    <address class="office-address">
      <span class="office-name">Sydney Office</span>
      <span>217 Kestrel Lane</span>
      <span>Marlow Heights, NSW</span>
      <span>Australia</span>
      <span>2188</span>
    </address>
  </main>
</body>
</html>
```